Boat Charter Power Point Template

Power Point Template for a Catalogue for a Boat Charter Company. In each slide there will be a main foto of the boat and then 3 mini photos plus all the aditional information of each boat. Here I attach 2 diferent presentations to get inspired

```html
<!DOCTYPE html>
<html lang="en">
<head>
<meta charset="utf-8">
<title>Boat Charter Company – Catalogue Template</title>
<link rel="stylesheet" href="https://fonts.googleapis.com/css2?family=Oswald:wght@300;500;600&family=Poppins:ital,wght@0,300;0,400;0,500;0,600;1,300&display=swap">
<style>
  :root{
    --blue:#0aa2f2;
    --navy:#16285a;
    --ink:#1d1d1f;
    --paper:#f5f5f6;
    --paper-soft:#e9e9eb;
    --sea-dark:#2f3a3c;
    --sea-mid:#46585a;
    --lagoon:#1aa6b4;
  }
  *{box-sizing:border-box;margin:0;padding:0}
  html,body{width:1200px;height:1164px;overflow:hidden;background:#ffffff}
  body{position:relative;font-family:"Poppins",sans-serif;color:var(--ink)}

  /* ---------- cover slide ---------- */
  .cover{position:absolute;left:300px;top:40px;width:600px;height:338px;overflow:hidden;
    background:linear-gradient(125deg,var(--sea-mid) 0%,var(--sea-dark) 55%,#262e30 100%);
    box-shadow:0 6px 18px rgba(0,0,0,.18)}
  .cover-frame{position:absolute;inset:0}
  .cover-title{position:absolute;left:265px;top:80px;font-family:"Oswald",sans-serif;font-weight:600;
    font-size:22px;line-height:29px;color:var(--navy);letter-spacing:0}
  .cover-tagline{position:absolute;left:265px;top:176px;font-style:italic;font-weight:300;
    font-size:15px;line-height:20px;color:#ffffff}
  .contact-pill{position:absolute;left:439px;top:137px;width:161px;height:64px;background:var(--blue);
    border-radius:32px 0 0 32px;padding:12px 0 0 22px;color:#fff;font-weight:600;font-size:10.5px;line-height:23px}
  .contact-pill .row{display:flex;align-items:center;gap:6px;white-space:nowrap}
  .contact-pill svg{width:12px;height:12px;flex:none}

  /* ---------- content slides ---------- */
  .slide{position:absolute;width:540px;height:304px;overflow:hidden;
    background:
      radial-gradient(ellipse 60% 40% at 20% 30%,#ffffff 0%,rgba(255,255,255,0) 70%),
      radial-gradient(ellipse 50% 45% at 75% 80%,#ffffff 0%,rgba(255,255,255,0) 70%),
      linear-gradient(160deg,var(--paper) 0%,var(--paper-soft) 100%);
    box-shadow:0 4px 12px rgba(0,0,0,.16)}
  .slide--welcome{left:45px;top:414px}
  .slide--ostralis{left:615px;top:414px}
  .slide--velantor{left:45px;top:748px}
  .slide--quorrana{left:615px;top:748px}

  .frame-top{position:absolute;left:308px;top:0;right:0;height:6px;background:var(--blue)}
  .frame-right{position:absolute;top:0;right:0;bottom:0;width:7px;background:var(--blue)}
  .frame-bottom{position:absolute;left:308px;bottom:0;right:0;height:6px;background:var(--blue)}
  .title-dash{position:absolute;left:0;top:32px;width:24px;height:5px;background:var(--blue)}
  .slide-title{position:absolute;left:32px;top:20px;font-family:"Oswald",sans-serif;font-size:19px;
    line-height:26px;font-weight:300;color:var(--ink);letter-spacing:.2px;white-space:nowrap}
  .slide-title .brand{color:var(--blue);font-weight:500}
  .slide-title .size{font-weight:600}
  .page-no{position:absolute;left:10px;bottom:0;width:24px;height:22px;background:var(--blue);
    color:#fff;font-size:7px;font-weight:600;display:flex;align-items:center;justify-content:center}

  /* welcome */
  .intro{position:absolute;left:37px;top:84px;width:174px;font-size:7.8px;line-height:9.2px;color:var(--ink)}
  .intro-lead{margin-bottom:5px}
  .intro-lead b{color:var(--blue);font-weight:600}
  .intro-list{list-style:none}
  .intro-list li{position:relative;padding-left:17px;margin-bottom:8px;text-align:justify}
  .intro-list li svg{position:absolute;left:0;top:1px;width:12px;height:6px}
  .welcome-block{position:absolute;left:310px;top:49px;width:167px;height:207px;background:var(--blue)}
  .welcome-photo{position:absolute;left:282px;top:64px;width:177px;height:177px;
    background:linear-gradient(180deg,#3f7fc6 0%,#a9c7e4 38%,#2f7fb0 55%,#c89a63 85%,#b8834e 100%)}

  /* boat spec table */
  .specs{position:absolute;left:50px;top:93px;font-size:7.8px;line-height:18.3px;border-collapse:collapse}
  .specs td{padding:0;vertical-align:middle;white-space:nowrap}
  .specs .ico{width:20px}
  .specs .ico svg{width:10px;height:10px;display:block}
  .specs .label{width:102px;color:var(--ink);font-weight:400}
  .specs .value{font-weight:500}
  .specs .value.note{font-size:5.8px;line-height:6.8px;font-weight:600;white-space:normal;width:80px;padding-top:4px;vertical-align:top}

  .boat-block{position:absolute;left:356px;top:74px;width:110px;height:156px;background:var(--blue)}
  .boat-photo{position:absolute;left:255px;top:83px;width:202px;height:137px}
  .mini{position:absolute;width:76px;height:58px;box-shadow:0 3px 6px rgba(0,0,0,.3)}
  .mini--top{left:411px;top:39px}
  .mini--mid{left:442px;top:123px}
  .mini--low{left:411px;top:208px}

  .tone-sea{background:linear-gradient(180deg,#8ec9ec 0%,#2fa3d6 45%,#155d9a 100%)}
  .tone-deck{background:linear-gradient(180deg,#8fc6e6 0%,#d9dcdc 50%,#8a8f93 100%)}
  .tone-galley{background:linear-gradient(135deg,#3a3532 0%,#bfb7ab 55%,#e8e2d8 100%)}
  .tone-cabin{background:linear-gradient(180deg,#6b4c34 0%,#c9a27c 55%,#efe5d6 100%)}
  .tone-bath{background:linear-gradient(180deg,#d9d2c4 0%,#f1eee8 60%,#c8c3b8 100%)}
</style>
</head>
<body>

<svg width="0" height="0" style="position:absolute" aria-hidden="true">
  <defs>
    <symbol id="i-cloud" viewBox="0 0 10 10"><path d="M2.3 6.2a1.8 1.8 0 0 1 .3-3.6A2.4 2.4 0 0 1 7 2.3a1.9 1.9 0 0 1 .6 3.9z" fill="#1d1d1f"/><path d="M3 7.5l-.5 1.5M5 7.5l-.5 1.5M7 7.5l-.5 1.5" stroke="#1d1d1f" stroke-width=".7"/></symbol>
    <symbol id="i-drops" viewBox="0 0 10 10"><circle cx="3.4" cy="3.4" r="2" fill="#1d1d1f"/><path d="M7 4.5c1 1.4 1.6 2.3 1.6 3a1.6 1.6 0 0 1-3.2 0c0-.7.6-1.6 1.6-3z" fill="#1d1d1f"/></symbol>
    <symbol id="i-sun" viewBox="0 0 10 10"><circle cx="5" cy="5" r="2.2" fill="#1d1d1f"/><path d="M5 .5v1.6M5 7.9v1.6M.5 5h1.6M7.9 5h1.6M1.8 1.8l1.1 1.1M7.1 7.1l1.1 1.1M1.8 8.2l1.1-1.1M7.1 2.9l1.1-1.1" stroke="#1d1d1f" stroke-width=".8"/></symbol>
    <symbol id="i-people" viewBox="0 0 10 10"><circle cx="5" cy="2.6" r="1.5" fill="#1d1d1f"/><circle cx="2" cy="3.6" r="1.1" fill="#1d1d1f"/><circle cx="8" cy="3.6" r="1.1" fill="#1d1d1f"/><path d="M2.8 9V6.2a2.2 2.2 0 0 1 4.4 0V9zM.3 9V6.5a1.6 1.6 0 0 1 2-1.5V9zM9.7 9V6.5a1.6 1.6 0 0 0-2-1.5V9z" fill="#1d1d1f"/></symbol>
    <symbol id="i-fuel" viewBox="0 0 10 10"><path d="M2 1h4v8H2zM6 3l2 1.5V8a.8.8 0 0 1-1.6 0V6H6" fill="#1d1d1f" stroke="#1d1d1f" stroke-width=".5"/></symbol>
    <symbol id="i-ship" viewBox="0 0 10 10"><path d="M3 2h3v1.6H3zM1.5 4h6l1 1.8H.8z" fill="#1d1d1f"/><path d="M.5 7.5c1 .8 2 .8 3 0s2-.8 3 0 2 .8 3 0" stroke="#1d1d1f" stroke-width=".8" fill="none"/></symbol>
    <symbol id="i-plus" viewBox="0 0 10 10"><circle cx="5" cy="5" r="4.5" fill="#1d1d1f"/><path d="M5 2.6v4.8M2.6 5h4.8" stroke="#fff" stroke-width="1.1"/></symbol>
    <symbol id="i-wave" viewBox="0 0 12 6"><path d="M0 5.5l2.5-4.5h9L9 5.5z" fill="#0aa2f2"/><path d="M2.5 3.2h7" stroke="#fff" stroke-width=".6"/></symbol>
  </defs>
</svg>

<!-- Cover -->
<section class="cover" aria-label="Cover slide">
  <svg class="cover-frame" width="600" height="338" viewBox="0 0 600 338">
    <path d="M0 0h260v8H8v322h252v8H0z" fill="var(--blue)"/>
    <rect x="8" y="8" width="584" height="322" fill="none" stroke="var(--blue)" stroke-width="1.5"/>
    <path d="M260 29a140 140 0 0 0 0 280z" fill="var(--lagoon)" role="img" aria-label="Aerial photo of a white motor yacht on turquoise water"/>
    <path d="M260 61a108 108 0 0 1 0 216z" fill="var(--blue)"/>
  </svg>
  <h1 class="cover-title">BOAT<br>CHARTER<br>COMPANY</h1>
  <p class="cover-tagline">More than<br>120 boats<br>Fin out!</p>
  <div class="contact-pill">
    <div class="row"><svg viewBox="0 0 12 12"><path d="M3 1l1.8 2.6-1 1.2a7 7 0 0 0 3.4 3.4l1.2-1L11 9l-1 2C5 11 1 7 1 2z" fill="none" stroke="#fff" stroke-width="1.1"/></svg>+(00) 123 456 7890</div>
    <div class="row"><svg viewBox="0 0 12 12"><circle cx="6" cy="6" r="5" fill="none" stroke="#fff" stroke-width="1.1"/><path d="M1 6h10M6 1c-2.5 3-2.5 7 0 10M6 1c2.5 3 2.5 7 0 10" fill="none" stroke="#fff" stroke-width=".9"/></svg>www.yoursite.com</div>
  </div>
</section>

<!-- Welcome -->
<section class="slide slide--welcome" aria-label="Welcome slide">
  <div class="frame-top"></div><div class="frame-right"></div><div class="frame-bottom"></div>
  <div class="title-dash"></div>
  <h2 class="slide-title"><span class="brand">WELCOME</span> ON BOARD !</h2>
  <div class="intro">
    <p class="intro-lead">The Sea is our <b>PASSION...</b></p>
    <ul class="intro-list">
      <li><svg><use href="#i-wave"/></svg>We want to offer a unique experience on our fleet of fully equipped boats.</li>
      <li><svg><use href="#i-wave"/></svg>Our goal is your enjoyment or relaxation, if we are able to do it, we are satisfied.</li>
      <li><svg><use href="#i-wave"/></svg>We hope you appreciate the quality of our services, all created specifically for our customers to organize your holidays or events.</li>
      <li><svg><use href="#i-wave"/></svg>Have confidence in us and we will make this experience unforgettable.</li>
    </ul>
  </div>
  <div class="welcome-block"></div>
  <div class="welcome-photo" role="img" aria-label="Photo of a yacht bow with teak deck facing a marina under blue sky"></div>
  <div class="page-no">2</div>
</section>

<!-- Ostralis -->
<section class="slide slide--ostralis" aria-label="Ostralis 90 Nerea">
  <div class="frame-top"></div><div class="frame-right"></div><div class="frame-bottom"></div>
  <div class="title-dash"></div>
  <h2 class="slide-title"><span class="brand">OSTRALIS</span> <span class="size">90</span> NEREA</h2>
  <table class="specs">
    <tr><td class="ico"><svg><use href="#i-cloud"/></svg></td><td class="label">HIGH SEASON</td><td class="value">9.499 €/day</td></tr>
    <tr><td class="ico"><svg><use href="#i-drops"/></svg></td><td class="label">MID SEASON</td><td class="value">7.899 €/day</td></tr>
    <tr><td class="ico"><svg><use href="#i-sun"/></svg></td><td class="label">LOW SEASON</td><td class="value">7.299 €/day</td></tr>
    <tr><td class="ico"><svg><use href="#i-people"/></svg></td><td class="label">CAPACITY</td><td class="value">12 + 3 Crew</td></tr>
    <tr><td class="ico"><svg><use href="#i-fuel"/></svg></td><td class="label">FUEL CONS</td><td class="value">600 L/h, 1.350 €</td></tr>
    <tr><td class="ico"><svg><use href="#i-ship"/></svg></td><td class="label">LENGHT/BEAM</td><td class="value">27 m/ 6,5 m</td></tr>
    <tr><td class="ico"><svg><use href="#i-plus"/></svg></td><td class="label">INCLUDED</td><td class="value note">Snorkeling equipment, Paddle boards, Sea scooter, Jet sky</td></tr>
  </table>
  <div class="boat-block"></div>
  <div class="boat-photo tone-sea" role="img" aria-label="Photo of a dark grey motor yacht cruising on turquoise sea"></div>
  <div class="mini mini--top tone-deck" role="img" aria-label="Photo of the aft deck lounge"></div>
  <div class="mini mini--mid tone-galley" role="img" aria-label="Photo of the galley"></div>
  <div class="mini mini--low tone-cabin" role="img" aria-label="Photo of a guest cabin"></div>
  <div class="page-no">3</div>
</section>

<!-- Velantor -->
<section class="slide slide--velantor" aria-label="Velantor 90 Blue Groove">
  <div class="frame-top"></div><div class="frame-right"></div><div class="frame-bottom"></div>
  <div class="title-dash"></div>
  <h2 class="slide-title"><span class="brand">VELANTOR</span> <span class="size">90</span> BLUE GROOVE</h2>
  <table class="specs">
    <tr><td class="ico"><svg><use href="#i-cloud"/></svg></td><td class="label">HIGH SEASON</td><td class="value">9.499 €/day</td></tr>
    <tr><td class="ico"><svg><use href="#i-drops"/></svg></td><td class="label">MID SEASON</td><td class="value">7.899 €/day</td></tr>
    <tr><td class="ico"><svg><use href="#i-sun"/></svg></td><td class="label">LOW SEASON</td><td class="value">7.299 €/day</td></tr>
    <tr><td class="ico"><svg><use href="#i-people"/></svg></td><td class="label">CAPACITY</td><td class="value">12 + 3 Crew</td></tr>
    <tr><td class="ico"><svg><use href="#i-fuel"/></svg></td><td class="label">FUEL CONS</td><td class="value">600 L/h, 1.350 €</td></tr>
    <tr><td class="ico"><svg><use href="#i-ship"/></svg></td><td class="label">LENGHT/BEAM</td><td class="value">27,5 m/ 6,5 m</td></tr>
    <tr><td class="ico"><svg><use href="#i-plus"/></svg></td><td class="label">INCLUDED</td><td class="value note">Snorkeling equipment, Paddle boards, Sea scooter, Jet scooter</td></tr>
  </table>
  <div class="boat-block"></div>
  <div class="boat-photo tone-sea" role="img" aria-label="Photo of a white and navy motor yacht at anchor in deep blue water"></div>
  <div class="mini mini--top tone-deck" role="img" aria-label="Photo of the outdoor dining deck"></div>
  <div class="mini mini--mid tone-cabin" role="img" aria-label="Photo of the main salon"></div>
  <div class="mini mini--low tone-galley" role="img" aria-label="Photo of the master cabin"></div>
  <div class="page-no">4</div>
</section>

<!-- Quorrana -->
<section class="slide slide--quorrana" aria-label="Quorrana 80 Sun Hour">
  <div class="frame-top"></div><div class="frame-right"></div><div class="frame-bottom"></div>
  <div class="title-dash"></div>
  <h2 class="slide-title"><span class="brand">QUORRANA</span> <span class="size">80</span> SUN HOUR</h2>
  <table class="specs">
    <tr><td class="ico"><svg><use href="#i-cloud"/></svg></td><td class="label">HIGH SEASON</td><td class="value">7.999 €/day</td></tr>
    <tr><td class="ico"><svg><use href="#i-drops"/></svg></td><td class="label">MID SEASON</td><td class="value">6.599 €/day</td></tr>
    <tr><td class="ico"><svg><use href="#i-sun"/></svg></td><td class="label">LOW SEASON</td><td class="value">5.899 €/day</td></tr>
    <tr><td class="ico"><svg><use href="#i-people"/></svg></td><td class="label">CAPACITY</td><td class="value">12 + 3 Crew</td></tr>
    <tr><td class="ico"><svg><use href="#i-fuel"/></svg></td><td class="label">FUEL CONS</td><td class="value">450 L/h, 900 €</td></tr>
    <tr><td class="ico"><svg><use href="#i-ship"/></svg></td><td class="label">LENGHT/BEAM</td><td class="value">24 m/ 6 m</td></tr>
    <tr><td class="ico"><svg><use href="#i-plus"/></svg></td><td class="label">INCLUDED</td><td class="value note">Snorkeling equipment, Paddle boards, Sea scooter</td></tr>
  </table>
  <div class="boat-block"></div>
  <div class="boat-photo tone-sea" role="img" aria-label="Photo of a white motor yacht speeding along a coastline"></div>
  <div class="mini mini--top tone-deck" role="img" aria-label="Photo of the flybridge deck"></div>
  <div class="mini mini--mid tone-cabin" role="img" aria-label="Photo of a double cabin"></div>
  <div class="mini mini--low tone-bath" role="img" aria-label="Photo of the bathroom"></div>
  <div class="page-no">5</div>
</section>

</body>
</html>
```